Personal Business Card Design Project

I am looking for a business card to be able to hand to both Chinese and Australian businessman.
I am a self employed consultant and just need my name, phone number and email address on the card. No Business Name and No Website.
I want it to look like an exclusive prestigious card.
I would like the background to be be a glossy red and the writing to be gold. (This applies to both sides of the card).
It must have English on one side and Chinese (Mandarin) on the reverse.
Details you will require
Name : Wade Emmerson
Phone : + 61 493 207 158
Email : wadeyemmerson@brightpost.example
Thank you everybody for your designs.
Industry/Entity Type
Business

```html
<!DOCTYPE html>
<html lang="en">
<head>
<meta charset="utf-8">
<title>Wade Emmerson – Business Card</title>
<link rel="stylesheet" href="https://fonts.googleapis.com/css2?family=Jost:wght@400;500&display=swap">
<style>
  :root {
    --backdrop: #b3b3b3;
    --frame: #000000;
    --red-glow: #cc1e26;
    --red-mid: #bb1a22;
    --red-edge: #94141a;
    --gold: #ecbb4e;
    --gold-shadow: rgba(60, 0, 0, 0.55);
    --red-emboss: #a3262a;
  }
  html, body {
    margin: 0;
    padding: 0;
    width: 1200px;
    height: 1067px;
    overflow: hidden;
    background: var(--backdrop);
  }
  .business-card {
    position: absolute;
    left: 150px;
    top: 256px;
    width: 900px;
    height: 554px;
    background: var(--frame);
  }
  .card-face {
    position: absolute;
    left: 73px;
    top: 68px;
    width: 757px;
    height: 423px;
    overflow: hidden;
    background: radial-gradient(ellipse 70% 75% at 52% 40%, var(--red-glow) 0%, var(--red-mid) 55%, var(--red-edge) 100%);
    font-family: "Jost", "Futura", sans-serif;
  }
  .side-name {
    position: absolute;
    left: 1px;
    bottom: 6px;
    margin: 0;
    writing-mode: vertical-rl;
    transform: rotate(180deg);
    font-size: 44px;
    font-weight: 400;
    line-height: 1;
    letter-spacing: 0;
    color: var(--red-emboss);
    white-space: nowrap;
  }
  .holder-name {
    position: absolute;
    right: 46px;
    top: 165px;
    margin: 0;
    font-size: 37px;
    font-weight: 500;
    line-height: 1;
    color: var(--gold);
    text-shadow: 2px 3px 4px var(--gold-shadow);
    white-space: nowrap;
  }
  .contact-list {
    position: absolute;
    right: 46px;
    top: 308px;
    margin: 0;
    padding: 0;
    list-style: none;
    text-align: right;
    font-size: 24px;
    font-weight: 400;
    line-height: 36px;
    color: var(--gold);
    white-space: nowrap;
  }
</style>
</head>
<body>
  <article class="business-card">
    <div class="card-face">
      <p class="side-name">WADE EMMERSON</p>
      <h1 class="holder-name">WADE EMMERSON</h1>
      <ul class="contact-list">
        <li class="contact-phone">+ 61 493 207 158</li>
        <li class="contact-email">wadeyemmerson@brightpost.example</li>
      </ul>
    </div>
  </article>
</body>
</html>
```